Logo needed for business card

Velquist Pty Ltd is in the business of healthcare and ecommerce.

We own and manage pharmacies and online health ecomerce sites.

We provide ecommerce consultants for companies looking for an ecommerce business startegy.

Think of it as the umbrella under which several healthcare brands may sit.

When I think of Velquist, I visulaise slick black/metalic colours, so please stay away from the common blue and green colours that seem to be so popular in this field.

Target Market(s)

CEOs and COOs

Industry/Entity Type

Healthcare

Contact Information for Business Card

Tessa Lindqvist
Director
Velquist Pty Ltd
4/362 Fennick Pde
Brellton, NSW 2148

Requirements
Must have
• Design must have scope to be implemented on the company's website and letterheads etc.

```html
<!DOCTYPE html>
<html lang="en">
<head>
<meta charset="utf-8">
<title>Velquist Pty Ltd — Business Card</title>
<link rel="stylesheet" href="https://fonts.googleapis.com/css2?family=Open+Sans:wght@600;700&display=swap">
<style>
  :root {
    --backdrop: #d9dcdb;
    --card-dark: #4a4a4a;
    --card-dark-edge: #2e2e2e;
    --card-light: #f4f4f4;
    --ink-light: #e9e9e9;
    --ink-dark: #3a3a3a;
    --ink-mid: #555555;
    --brand-font: "Open Sans", Arial, sans-serif;
  }
  * { margin: 0; padding: 0; box-sizing: border-box; }
  html, body {
    width: 1200px;
    height: 900px;
    overflow: hidden;
    background: var(--backdrop);
    font-family: var(--brand-font);
  }
  .canvas {
    position: relative;
    width: 1200px;
    height: 900px;
  }
  .card {
    position: absolute;
    left: 320px;
    width: 560px;
    height: 320px;
    border-radius: 4px;
    box-shadow: 0 10px 28px rgba(0,0,0,0.22);
  }
  .card--front {
    top: 100px;
    background: linear-gradient(160deg, #555555 0%, var(--card-dark) 55%, #3d3d3d 100%);
    border: 1px solid var(--card-dark-edge);
    display: flex;
    align-items: center;
    justify-content: center;
  }
  .card--back {
    top: 480px;
    background: var(--card-light);
  }
  .wordmark {
    display: flex;
    align-items: center;
    gap: 14px;
  }
  .wordmark__dot {
    width: 34px;
    height: 34px;
    border-radius: 50%;
  }
  .wordmark__name {
    font-weight: 700;
    white-space: nowrap;
    letter-spacing: 0.5px;
  }
  .card--front .wordmark__dot { background: var(--ink-light); }
  .card--front .wordmark__name { color: var(--ink-light); font-size: 40px; }
  .card--back .wordmark {
    position: absolute;
    top: 46px;
    right: 40px;
    gap: 10px;
  }
  .card--back .wordmark__dot { width: 24px; height: 24px; background: var(--ink-mid); }
  .card--back .wordmark__name { color: var(--ink-mid); font-size: 28px; }
  .contact {
    position: absolute;
    left: 44px;
    bottom: 40px;
    color: var(--ink-dark);
  }
  .contact__name {
    font-size: 30px;
    font-weight: 700;
    line-height: 1.1;
  }
  .contact__role {
    font-size: 17px;
    font-weight: 700;
    margin-bottom: 26px;
  }
  .contact__address {
    display: flex;
    align-items: center;
    gap: 8px;
    font-size: 14px;
    font-weight: 600;
    color: var(--ink-mid);
  }
  .contact__pin { width: 12px; height: 16px; }
</style>
</head>
<body>
  <main class="canvas">
    <section class="card card--front">
      <div class="wordmark">
        <span class="wordmark__dot"></span>
        <span class="wordmark__name">Velquist Pty Ltd</span>
      </div>
    </section>

    <section class="card card--back">
      <div class="wordmark">
        <span class="wordmark__dot"></span>
        <span class="wordmark__name">Velquist Pty Ltd</span>
      </div>
      <div class="contact">
        <p class="contact__name">Tessa Lindqvist</p>
        <p class="contact__role">Director</p>
        <p class="contact__address">
          <svg class="contact__pin" viewBox="0 0 12 16" aria-hidden="true">
            <path d="M6 0.8C3.1 0.8 0.9 3 0.9 5.8 0.9 9.6 6 15.2 6 15.2S11.1 9.6 11.1 5.8C11.1 3 8.9 0.8 6 0.8Z" fill="none" stroke="#3a3a3a" stroke-width="1.6"/>
            <circle cx="6" cy="5.8" r="1.8" fill="#3a3a3a"/>
          </svg>
          4/362 Fennick Pde Brellton, NSW 2148
        </p>
      </div>
    </section>
  </main>
</body>
</html>
```